Graphic design for Facebook Post for Brightnook

We need a great looking graphic to post on our facebook page. This post should convey one of our taglines and or hashtag :
#Glide7Aid
"Life is but a Stream"
This Post should have a teenage girl or teenage girl and boy potentially. or some imagery that conveys visually ; safety, mobile video, GPS and definitely have our product logo/icon present.

Target Market(s)

18-55 years old

Colors
0792cd

Requirements
Must have
• a great look and illicit and provoke emotion and compel the viewer to want be emotionally invested.

```html
<!DOCTYPE html>
<html lang="en">
<head>
<meta charset="utf-8">
<title>Brightnook – #Glide7Aid</title>
<link href="https://fonts.googleapis.com/css2?family=Poppins:wght@300;500;600;700&display=swap" rel="stylesheet">
<style>
  :root {
    --chip-blue: #3352d6;
    --play-red: #f0505a;
    --pin-red: #e0474f;
    --halo-blue: #4fb3e8;
    --halo-core: #1aa7f0;
    --band-left: #5062b6;
    --band-right: #4a90d2;
    --brand-blue: #2f52d6;
    --white: #ffffff;
    --pink-soft: rgba(236, 186, 200, 0.55);
    --lilac-soft: rgba(214, 196, 224, 0.45);
  }
  * { margin: 0; padding: 0; box-sizing: border-box; }
  html, body { width: 1200px; height: 1200px; overflow: hidden; background: var(--white); }
  .post {
    position: relative;
    width: 1200px;
    height: 1200px;
    overflow: hidden;
    font-family: "Poppins", sans-serif;
  }
  .hero-photo {
    position: absolute;
    inset: 0 0 300px 0;
    background:
      radial-gradient(ellipse 380px 520px at 640px 560px, #e9e4e6 0%, rgba(233,228,230,0) 70%),
      radial-gradient(ellipse 260px 200px at 470px 560px, #c99a82 0%, rgba(201,154,130,0) 75%),
      linear-gradient(100deg, #d9d3d2 0%, #ece6e6 45%, #e6dde0 75%, #eadfe2 100%);
  }
  .decor { position: absolute; inset: 0; }
  .chip {
    position: absolute;
    height: 66px;
    display: flex;
    align-items: center;
    background: var(--chip-blue);
    border-radius: 33px;
    color: var(--white);
    padding-right: 34px;
  }
  .chip-play {
    width: 66px; height: 66px;
    border-radius: 50%;
    background: var(--white);
    display: flex; align-items: center; justify-content: center;
    margin-right: 22px;
  }
  .chip-name { font-weight: 700; font-size: 28px; letter-spacing: 0.5px; }
  .chip-live {
    display: flex; align-items: center;
    margin-left: auto;
    font-weight: 600; font-size: 16px; letter-spacing: 0.5px;
  }
  .chip-live::before {
    content: "";
    width: 14px; height: 14px;
    border-radius: 50%;
    background: var(--play-red);
    margin-right: 10px;
  }
  .chip--dad { left: 333px; top: 198px; width: 265px; }
  .chip--mom { left: 89px; top: 343px; width: 269px; }
  .chip--henry { left: 618px; top: 420px; width: 290px; }
  .headline {
    position: absolute;
    left: 86px; top: 792px;
    font-weight: 600;
    font-size: 108px;
    line-height: 1;
    color: var(--white);
    letter-spacing: 0.5px;
  }
  .tagline {
    position: absolute;
    left: 89px; top: 932px;
    font-weight: 300;
    font-size: 60px;
    line-height: 1;
    color: var(--white);
  }
  .brand {
    position: absolute;
    right: 48px; top: 1100px;
    display: flex; align-items: center;
    gap: 14px;
    font-weight: 600;
    font-size: 50px;
    color: var(--brand-blue);
  }
  .brand-dot { width: 30px; height: 30px; border-radius: 50%; background: var(--brand-blue); }
</style>
</head>
<body>
<main class="post">
  <div class="hero-photo" role="img" aria-label="Photo of a young man in a light t-shirt with sunglasses hooked on the collar, holding a smartphone with both hands"></div>

  <svg class="decor" width="1200" height="1200" viewBox="0 0 1200 1200" aria-hidden="true">
    <defs>
      <linearGradient id="band-gradient" x1="0" y1="1" x2="1" y2="0">
        <stop offset="0" stop-color="var(--band-left)"/>
        <stop offset="1" stop-color="var(--band-right)"/>
      </linearGradient>
    </defs>
    <circle class="pink-circle" cx="760" cy="-360" r="520" fill="var(--pink-soft)"/>
    <circle class="lilac-circle" cx="1280" cy="260" r="430" fill="var(--lilac-soft)"/>
    <ellipse class="location-halo" cx="459" cy="426" rx="144" ry="78" fill="var(--halo-blue)" opacity="0.85"/>
    <ellipse class="location-core" cx="453" cy="426" rx="64" ry="30" fill="var(--halo-core)"/>
    <path class="location-pin" d="M458 428 C440 396 402 370 402 334 A56 56 0 0 1 514 334 C514 370 476 396 458 428 Z" fill="var(--pin-red)"/>
    <circle cx="458" cy="334" r="20" fill="var(--white)"/>
    <polygon class="title-band" points="0,767 1200,667 1200,1200 0,1200" fill="url(#band-gradient)"/>
    <polygon class="corner-white" points="1200,889 1200,1200 478,1200" fill="var(--white)"/>
  </svg>

  <div class="chip chip--dad">
    <span class="chip-play"><svg width="24" height="26" viewBox="0 0 24 26"><polygon points="2,1 23,13 2,25" fill="var(--play-red)"/></svg></span>
    <span class="chip-name">Dad</span>
    <span class="chip-live">LIVE</span>
  </div>
  <div class="chip chip--mom">
    <span class="chip-play"><svg width="24" height="26" viewBox="0 0 24 26"><polygon points="2,1 23,13 2,25" fill="var(--play-red)"/></svg></span>
    <span class="chip-name">Mom</span>
    <span class="chip-live">LIVE</span>
  </div>
  <div class="chip chip--henry">
    <span class="chip-play"><svg width="24" height="26" viewBox="0 0 24 26"><polygon points="2,1 23,13 2,25" fill="var(--play-red)"/></svg></span>
    <span class="chip-name">Henry</span>
    <span class="chip-live">LIVE</span>
  </div>

  <h1 class="headline">#Glide7Aid</h1>
  <p class="tagline">"Life is but a Stream"</p>

  <div class="brand"><span class="brand-dot"></span>Brightnook</div>
</main>
</body>
</html>
```